DVD / USB CASE COVER For Educational Software

We are an educational software company
Until today we supplied our software to clients on 5 DVDs
We are now going to combine all the 5 DVDs into a single USB flash drive - The flash drive will be packaged in a Case similar to A DVD case (see image "case sample")
We looking for a new updated design for the USB case to combine and replace all our 5 DVDs (see attached current DVDs artwork)
The new design does not need to be similar to the old ones but it should be related to the topics of our programs :
Maths
English
Afrikaans
Study methods
Accounting (grade 12 only)
Science (Grade 12 only)
Please see attached our logo as well
Please go into our website to the video section http://www.brightquillza.co.za/videos/
to get a feeling of what our software is about
The design should be single sided.
Case size 189 X 273MM

Target Market(s)

Parents to vhilden in school

Industry/Entity Type

Software

Colors

Designer to choose colors to be used in the design.

Requirements
Must have
• Details of the topics of our programs :
• Maths
• English
• Afrikaans
• Study methods
• Accounting (grade 12 only)
• Science (Grade 12 only)
• Case size 189 X 273MM
Nice to have
• A new fresh new look to give parents the feeling of a high qualty software that will help their children in school
Should not have
• please donst use the color yellow

```html
<!DOCTYPE html>
<html lang="en">
<head>
<meta charset="utf-8">
<title>Brightquill – Educational Software Case Cover</title>
<link href="https://fonts.googleapis.com/css2?family=Mulish:wght@400;500;600&display=swap" rel="stylesheet">
<style>
  :root{
    --back-blue:#1f4a8f;
    --spine-navy:#131c3c;
    --band-navy:rgba(24,38,74,.88);
    --band-cyan:#4cc4e8;
    --title-blue:#5cb6ea;
    --play-blue:#1aa3e6;
    --label-blue:#9fd2f2;
    --ink-dark:#13213f;
    --white:#ffffff;
  }
  *{margin:0;padding:0;box-sizing:border-box}
  html,body{width:1200px;height:831px;overflow:hidden;background:var(--back-blue)}
  body{font-family:"Mulish",sans-serif;color:var(--white)}
  .cover{position:relative;width:1200px;height:831px;overflow:hidden;
    background:linear-gradient(180deg,#21509a 0%,#1d4790 55%,#1c438a 100%)}
  .back-glow{position:absolute;left:0;top:118px;width:561px;height:240px;
    background:radial-gradient(ellipse at 60% 30%,rgba(120,170,230,.18),transparent 70%)}
  .logo-box{position:absolute;left:135px;top:240px;width:277px;height:49px;background:var(--white);
    display:flex;align-items:center;gap:10px;padding-left:14px}
  .logo-box .dot{width:22px;height:22px;border-radius:50%;background:var(--back-blue)}
  .logo-box .name{font-weight:600;font-size:24px;color:var(--back-blue);letter-spacing:1px}
  .specs{position:absolute;left:77px;top:340px;width:386px;font-size:10.8px;line-height:15.5px;
    text-transform:uppercase;text-align:justify;font-weight:500}
  .specs p+p{margin-top:15.5px}
  .origin{position:absolute;left:182px;top:598px;width:150px;height:33px;
    border-top:1px solid rgba(255,255,255,.8);border-bottom:1px solid rgba(255,255,255,.8);
    display:flex;align-items:center;gap:10px;font-size:11px}
  .origin svg{width:31px;height:18px}
  .av-badge{position:absolute;display:flex;align-items:center}
  .av-badge .play{width:46px;height:46px;border-radius:50%;background:var(--play-blue);
    border:2px solid #1665b8;display:flex;align-items:center;justify-content:center;position:relative;z-index:2}
  .av-badge .play svg{width:20px;height:22px;margin-left:4px}
  .av-badge .label{background:var(--label-blue);color:var(--ink-dark);font-size:14.5px;
    height:25px;line-height:25px;padding:0 7px 0 12px;margin-left:-6px;letter-spacing:.2px}
  .av-back{left:136px;top:721px}
  .av-front{left:793px;top:55px}
  .spine{position:absolute;left:561px;top:0;width:76px;height:831px;background:var(--spine-navy)}
  .spine-text{position:absolute;left:50%;top:428px;transform:translate(-50%,-50%) rotate(-90deg);
    white-space:nowrap;font-size:13.6px;font-weight:500;letter-spacing:.6px}
  .front{position:absolute;left:637px;top:0;width:563px;height:831px}
  .cyan-band{position:absolute;left:0;top:115px;width:563px;height:38px;
    background:linear-gradient(90deg,#2f7fc2,var(--band-cyan) 60%,#3aa8de)}
  .photo{position:absolute;left:0;top:316px;width:563px;height:434px;
    background:radial-gradient(ellipse at 40% 60%,#a8e6f2 0%,#5fc6e2 35%,#2d8cc4 70%,#1d5a9a 100%)}
  .title-band{position:absolute;left:0;top:153px;width:563px;height:163px;background:var(--band-navy);text-align:center}
  .subjects{position:absolute;left:0;width:100%;top:15px;color:var(--title-blue);font-size:24px;line-height:31px;font-weight:500;letter-spacing:.3px}
  .grade{position:absolute;top:120px;font-size:10.5px;font-weight:500}
  .grade.g1{left:163px}.grade.g2{left:324px}
  .arc{position:absolute;left:0;top:0;width:563px;height:831px}
  .footer-band{position:absolute;left:0;top:750px;width:563px;height:37px;background:var(--ink-dark);
    text-align:center;line-height:37px;font-size:19px;font-weight:500;letter-spacing:1.2px}
</style>
</head>
<body>
<main class="cover">
  <section class="back">
    <div class="back-glow"></div>
    <div class="logo-box"><span class="dot"></span><span class="name">Brightquill</span></div>
    <div class="specs">
      <p>The tablet has an 8-inch screen with WXGA (1280×800) resolution and a 16:10 aspect ratio for vivid picture quality to play, read, watch, stream or work. And is based on a Corvane™ Quad-Core CV3735 processor, 1.8GHz.</p>
      <p>The tablet has an 8-inch screen with WXGA (1280×800) resolution and a 16:10 aspect ratio for vivid picture quality to play, read, watch, stream or work. And is based on a Corvane™ Quad-Core CV3735 processor, 1.8GHz.</p>
    </div>
    <div class="origin">
      <svg viewBox="0 0 30 18" aria-hidden="true">
        <rect width="30" height="9" fill="#e03c31"/><rect y="9" width="30" height="9" fill="#1b3f95"/>
        <polygon points="0,0 13,9 0,18" fill="#111"/>
        <polygon points="0,2 10,9 0,16 0,18 3,18 13,11 30,11 30,7 13,7 3,0 0,0" fill="#fff"/>
        <polygon points="0,3 11,9 0,15" fill="#111"/>
        <path d="M0,0 L13,8 L30,8 L30,10 L13,10 L0,18 L0,16 L11,9 L0,2Z" fill="#007a4d"/>
      </svg>
      <span>Made in South Africa</span>
    </div>
    <div class="av-badge av-back">
      <span class="play"><svg viewBox="0 0 20 22"><polygon points="0,0 20,11 0,22" fill="#fff"/></svg></span>
      <span class="label">AUDIO VISUAL LEARNING</span>
    </div>
  </section>

  <aside class="spine">
    <div class="spine-text">MATHS &nbsp;I&nbsp; ENGLISH &nbsp;I&nbsp; AFRIKAANS &nbsp;I&nbsp; STUDY METHODS &nbsp;I&nbsp; ACCOUNTING &nbsp;I&nbsp; SCIENCE</div>
  </aside>

  <section class="front">
    <div class="cyan-band"></div>
    <div class="photo" role="img" aria-label="Open books stacked on a desk in soft cyan light"></div>
    <svg class="arc" viewBox="0 0 563 831" aria-hidden="true">
      <circle cx="300" cy="420" r="340" fill="none" stroke="rgba(220,240,255,.55)" stroke-width="2"/>
    </svg>
    <div class="title-band">
      <div class="subjects">
        <div>MATHS &nbsp;I&nbsp; ENGLISH</div>
        <div>AFRIKAANS &nbsp;I&nbsp; STUDY METHODS</div>
        <div>ACCOUNTING &nbsp;I&nbsp; SCIENCE</div>
      </div>
      <span class="grade g1">GRADE 12 ONLY</span>
      <span class="grade g2">GRADE 12 ONLY</span>
    </div>
    <div class="footer-band">EDUCATIONAL SOFTWARE</div>
  </section>

  <div class="av-badge av-front">
    <span class="play"><svg viewBox="0 0 20 22"><polygon points="0,0 20,11 0,22" fill="#fff"/></svg></span>
    <span class="label">AUDIO VISUAL LEARNING</span>
  </div>
</main>
</body>
</html>
```